New website for Pollard Law Firm at www.keepwinning-example.com

We are a professional law firm located in the Nashville, Tennessee USA area. We focus on personal injury law. We are looking for a slick new website that is user friendly for updating with new blogs, videos, etc. The primary colors should be red, black, and white. It should load extremely fast and have a good mobile component. The pages for the design will include a home page, about us, news, contact us, and practice page. The practice page will be copied for all the practice areas including motor vehicle accidents, slip and fall accidents, dog bites, etc. We have included an image which we would like to include in the new site which shows the color scheme The image is called banner-Car Wreck. The new website should NOT have gavels, court houses, law books, scales or the typical images for a law firm.

Target Market(s)

People in Tennessee involved in accidents

Industry/Entity Type

Legal services, law firm

Coding

Coded - Design and coding required

Number of Pages Required

5+ page

Font styles to use
Serif

Colors
EB3D1F
EC4F4E
F09395
F8D3D4
FCEDEE

Requirements
Should not have
• Gavels, columns, scales, law related images

```html
<!DOCTYPE html>
<html lang="en">
<head>
<meta charset="utf-8">
<title>Pollard Law Firm PLLC</title>
<link href="https://fonts.googleapis.com/css2?family=Open+Sans:wght@400;600;700&display=swap" rel="stylesheet">
<style>
:root{
  --red:#D8232A;
  --red-deep:#B81B21;
  --red-soft:#EC4F4E;
  --pink:#F8D3D4;
  --pink-light:#FCEDEE;
  --black:#0E0E0E;
  --dark:#1C1C1E;
  --white:#FFFFFF;
  --text:#333333;
  --muted:#6A6A6A;
  --line:#E6E6E6;
}
*{box-sizing:border-box;margin:0;padding:0}
html,body{width:1200px;height:4408px;overflow:hidden}
body{font-family:"Open Sans",Arial,sans-serif;color:var(--text);background:var(--white);position:relative}
.section{position:absolute;left:0;width:1200px}
.abs{position:absolute}
.btn{display:inline-block;background:var(--red);color:var(--white);font-size:13px;font-weight:600;padding:9px 22px;border-radius:2px;text-decoration:none}
.btn-small{font-size:10px;padding:5px 12px}
.eyebrow{font-size:13px;color:var(--text);text-align:center;letter-spacing:.5px}
.eyebrow::before,.eyebrow::after{content:"";display:inline-block;width:24px;height:1px;background:currentColor;vertical-align:middle;margin:0 10px}
.section-title{font-size:30px;font-weight:700;color:var(--red);text-align:center;margin-top:4px}
.photo{position:absolute}

/* header */
.site-header{top:0;height:60px;background:var(--white)}
.brand{left:230px;top:20px;display:flex;align-items:center;gap:8px;font-size:17px;font-weight:700;color:var(--red);line-height:1;white-space:nowrap}
.brand-mark{width:12px;height:12px;background:var(--red)}
.nav{right:230px;top:20px;display:flex;gap:26px;align-items:center;font-size:12px}
.nav a{color:var(--text);text-decoration:none}
.nav .btn{color:var(--white);padding:7px 16px;font-size:12px}

/* hero */
.hero{top:60px;height:530px;background:var(--black);overflow:hidden}
.hero-photo{left:460px;top:0;width:740px;height:530px;background:radial-gradient(ellipse at 60% 45%,#8E1A1E 0%,#4A0D10 40%,#0E0E0E 75%)}
.hero-kicker{left:230px;top:188px;font-size:14px;letter-spacing:2px;color:var(--red-soft)}
.hero-kicker::before{content:"";display:inline-block;width:30px;height:1px;background:var(--red-soft);vertical-align:middle;margin-right:10px}
.hero-title{left:230px;top:218px;width:400px;font-size:54px;line-height:1.1;font-weight:700;color:var(--white)}

/* cta band */
.cta{top:590px;height:190px;background:var(--red)}
.cta h2{left:230px;top:62px;font-size:25px;font-weight:700;color:var(--white)}
.cta p{left:230px;top:102px;width:420px;font-size:13px;color:var(--white);line-height:1.5}
.cta .btn{left:790px;top:75px;background:var(--white);color:var(--red);padding:10px 26px}

/* practice */
.practice{top:780px;height:610px}
.practice .eyebrow{position:absolute;left:0;width:1200px;top:92px}
.practice .section-title{position:absolute;left:0;width:1200px;top:108px}
.cards{left:248px;top:170px;display:flex;gap:14px}
.card{width:224px;height:318px;border:1px solid var(--line);background:var(--white);text-align:center;padding-top:26px;box-shadow:0 2px 8px rgba(0,0,0,.05)}
.card svg{display:block;margin:0 auto 12px}
.card h3{font-size:14px;font-weight:600;color:var(--text)}
.card p{font-size:10px;color:var(--muted);line-height:1.5;padding:6px 20px 4px}
.card .more{font-size:10px;color:var(--red);font-weight:600}
.card .thumb{width:194px;height:130px;margin:14px auto 0}
.practice .btn{left:545px;top:540px}

/* about */
.about{top:1390px;height:400px;background:var(--black);overflow:hidden}
.about-photo{left:0;top:0;width:700px;height:400px;background:linear-gradient(135deg,#2A2E36 0%,#151618 55%,#0B0B0B 100%)}
.play{left:410px;top:168px;width:68px;height:68px;border-radius:50%;background:rgba(255,255,255,.92)}
.about .eyebrow{position:absolute;left:710px;top:118px;color:var(--white);text-align:left}
.about h2{left:720px;top:140px;font-size:25px;color:var(--white);font-weight:700}
.about p{left:720px;top:186px;width:280px;font-size:10px;line-height:1.6;color:#C9C9C9}
.about .btn{left:720px;top:278px}

/* who we are */
.who{top:1790px;height:1050px}
.who .eyebrow{position:absolute;left:0;width:1200px;top:62px}
.who .section-title{position:absolute;left:0;width:1200px;top:78px;font-size:28px}
.who-photo{width:300px;height:288px}
.who-box{width:320px;height:216px;padding:24px 26px;font-size:10px;line-height:1.6}
.box-light{background:var(--white);border:2px solid var(--pink);box-shadow:0 4px 14px rgba(0,0,0,.06)}
.box-red{background:var(--red);color:var(--white)}

/* team */
.team{top:2840px;height:400px;background:var(--red)}
.team .eyebrow{position:absolute;left:0;width:1200px;top:64px;color:var(--white)}
.team h2{left:0;width:1200px;top:84px;text-align:center;color:var(--white);font-size:28px;font-weight:700}
.ring{width:164px;height:164px;border-radius:50%;background:var(--red-soft);border:6px solid var(--pink)}
.ring .face{position:absolute;left:16px;top:16px;width:120px;height:120px;border-radius:50%}
.member{left:500px;top:154px;width:200px;height:214px;background:var(--white);text-align:center;padding-top:20px}
.member .face{width:110px;height:110px;margin:0 auto}
.member h3{font-size:13px;font-weight:600;margin-top:12px;color:var(--text)}
.member span{display:block;font-size:9px;color:var(--muted);margin:2px 0 8px}

/* blog */
.blog{top:3240px;height:480px}
.blog .eyebrow{position:absolute;left:0;width:1200px;top:72px}
.blog .section-title{position:absolute;left:0;width:1200px;top:88px;font-size:28px}
.posts{left:248px;top:168px;display:flex;gap:14px}
.post{width:224px;height:250px;background:var(--white);border:1px solid var(--line);box-shadow:0 2px 8px rgba(0,0,0,.06);position:relative}
.post .thumb{height:150px;position:relative}
.date{position:absolute;right:12px;top:12px;width:42px;height:46px;background:var(--red);color:var(--white);text-align:center;font-size:9px;font-weight:700;line-height:1.2;padding-top:8px}
.post h3{font-size:11px;font-weight:700;padding:14px 16px 0 36px;line-height:1.4;color:var(--text)}
.post .btn{position:absolute;left:36px;bottom:16px}

/* footer */
.footer{top:3720px;height:630px;background:linear-gradient(180deg,#202024,#141416)}
.footer h2{left:230px;top:86px;font-size:24px;font-weight:400;color:var(--white)}
.footer .rule{left:230px;top:124px;width:30px;height:2px;background:var(--red)}
.footer .addr{left:230px;top:146px;font-size:10px;color:#BDBDBD;line-height:1.6;width:220px}
.contact-line{font-size:11px;color:#D5D5D5;display:flex;align-items:center;gap:8px}
.socials{left:230px;top:360px;display:flex;gap:10px}
.socials span{width:24px;height:24px;border-radius:50%;background:var(--red)}
.form{left:630px;top:62px;width:340px;height:496px;background:var(--red);padding:24px 22px}
.field{height:34px;border-bottom:1px solid rgba(255,255,255,.55);color:var(--white);font-size:11px;padding-top:10px;margin-bottom:10px}
.field.tall{height:110px}
.form small{display:block;font-size:8px;color:#FAD9DA;line-height:1.5;margin:10px 0 14px}
.submit{display:block;background:var(--white);color:var(--red);text-align:center;font-size:12px;font-weight:700;padding:9px 0}
.copyright{top:4350px;height:58px;background:var(--red);color:var(--white);font-size:11px;text-align:center;line-height:58px}
</style>
</head>
<body>

<header class="section site-header">
  <div class="abs brand"><span class="brand-mark"></span>Pollard Law Firm</div>
  <nav class="abs nav">
    <a href="#">Home</a><a href="#">About Us</a><a href="#">Blog</a><a href="#">Videos</a><a href="#">Practice Area</a><a href="#">Pages</a>
    <a class="btn" href="#">Contact Us</a>
  </nav>
</header>

<section class="section hero">
  <div class="abs hero-photo" role="img" aria-label="Close-up of a red car wrecked in a collision, shattered headlight"></div>
  <div class="abs hero-kicker">POLLARD LAW FIRM PLLC</div>
  <h1 class="abs hero-title">Don’t lose what’s legally yours</h1>
</section>

<section class="section cta">
  <h2 class="abs">The Attorneys You Want On Your Side</h2>
  <p class="abs">Lorem ipsum dolor sit amet, consectetur adipiscing elit, sed do eiusmod tempor incididunt ut labore et</p>
  <a class="abs btn" href="#">Free consultancy</a>
</section>

<section class="section practice">
  <div class="eyebrow">Services</div>
  <h2 class="section-title">Practice Areas</h2>
  <div class="abs cards">
    <article class="card">
      <svg width="34" height="30" viewBox="0 0 34 30" fill="none" stroke="#333" stroke-width="1.6"><path d="M4 20 L7 11 Q8 8 11 8 H23 Q26 8 27 11 L30 20 V25 H4 Z"/><circle cx="10" cy="21" r="2"/><circle cx="24" cy="21" r="2"/></svg>
      <h3>Motor vehicle accidents</h3>
      <p>Lorem ipsum dolor sit amet, consectetur adipiscing elit sed do eiusmod tempor</p>
      <div class="more">Read More</div>
      <div class="thumb" role="img" aria-label="Driver checking a damaged car after a crash" style="background:linear-gradient(135deg,#8A96A6,#3E4654)"></div>
    </article>
    <article class="card">
      <svg width="34" height="30" viewBox="0 0 34 30" fill="none" stroke="#333" stroke-width="1.6"><circle cx="14" cy="5" r="3"/><path d="M14 9 L18 17 L26 20 M16 13 L8 16 M18 17 L12 26 M4 28 H30"/></svg>
      <h3>slip and fall accidents</h3>
      <p>Lorem ipsum dolor sit amet, consectetur adipiscing elit sed do eiusmod tempor</p>
      <div class="more">Read More</div>
      <div class="thumb" role="img" aria-label="Wet floor warning sign on a slippery office floor" style="background:linear-gradient(135deg,#E9E2C8,#B9A764)"></div>
    </article>
    <article class="card">
      <svg width="34" height="30" viewBox="0 0 34 30" fill="none" stroke="#333" stroke-width="1.6"><path d="M6 14 Q6 6 14 6 L22 8 L28 14 L24 16 L20 14 L16 24 H8 Z"/><circle cx="21" cy="11" r="1"/></svg>
      <h3>dog bites</h3>
      <p>Lorem ipsum dolor sit amet, consectetur adipiscing elit sed do eiusmod tempor</p>
      <div class="more">Read More</div>
      <div class="thumb" role="img" aria-label="Aggressive dog outdoors near a person" style="background:linear-gradient(135deg,#9BB76A,#4F6E2E)"></div>
    </article>
  </div>
  <a class="abs btn" href="#">View More</a>
</section>

<section class="section about">
  <div class="abs about-photo" role="img" aria-label="Lawyer in a dark suit signing documents at a desk"></div>
  <svg class="abs play" viewBox="0 0 68 68"><path d="M28 22 L48 34 L28 46 Z" fill="#111"/></svg>
  <div class="eyebrow">About Us</div>
  <h2 class="abs">Pollard Law Firm PLLC</h2>
  <p class="abs">Lorem ipsum dolor sit amet, consectetur adipiscing elit sed do eiusmod tempor incididunt ut labore et dolore magna aliqua. Ut enim ad minim veniam, quis nostrud exercitation ullamco laboris nisi ut aliquip ex ea commodo consequat duis aute.</p>
  <a class="abs btn" href="#">View More</a>
</section>

<section class="section who">
  <div class="eyebrow">Who We Are</div>
  <h2 class="section-title">Trial Lawyers...</h2>

  <div class="photo who-photo" role="img" aria-label="Attorneys meeting with clients around an office table" style="left:230px;top:150px;background:linear-gradient(135deg,#6F7B8C,#2E3440)"></div>
  <div class="abs who-box box-light" style="left:560px;top:186px">We are trial lawyers and we are proud of it. There are many law firms in Tennessee who claim to be trial lawyers, but most attorneys have never seen a courtroom. We have tried hundreds of cases to verdict and we have helped thousands of people in this community recover. The fight against billion-dollar insurance companies, large corporations, and the State of Tennessee is one we know.</div>

  <div class="abs who-box box-red" style="left:260px;top:500px">If it’s your first time to visit a law firm, you probably have many questions and concerns. You may not know what your case is worth or how to find help you can trust. We listen carefully, explain every option in plain language, and make sure you feel heard, respected, and supported. The insurance company is already working to protect itself, and you deserve someone in your corner who fights just as hard.</div>
  <div class="photo who-photo" role="img" aria-label="Lawyer consulting with a young couple in an office" style="left:612px;top:466px;background:linear-gradient(135deg,#C9A98A,#6E4F3A)"></div>

  <div class="photo who-photo" role="img" aria-label="Senior partner reviewing papers with colleagues" style="left:230px;top:790px;background:linear-gradient(135deg,#BFC5CC,#5D646E)"></div>
  <div class="abs who-box box-light" style="left:560px;top:826px">Our motto is: There’s a Law What is Legally Yours. We are the only law firm in Tennessee with a website that says so. We strive to help our clients and do everything we can to make sure that they don’t lose the money they deserve. No matter what kind of injury you have suffered, we will work hard for a fair result, and we will do everything possible to protect your future.</div>
</section>

<section class="section team">
  <div class="eyebrow">Our Team</div>
  <h2 class="abs">Passion. Experience. Diligence.</h2>
  <div class="abs ring" style="left:300px;top:190px"><div class="face" role="img" aria-label="Portrait of a female attorney" style="background:linear-gradient(160deg,#D9B49A,#7A4E3A)"></div></div>
  <div class="abs member">
    <div class="face" role="img" aria-label="Portrait of attorney Daniel R. Pollard" style="background:linear-gradient(160deg,#CFCFCF,#5E5E5E)"></div>
    <h3>Daniel R. Pollard</h3>
    <span>Attorney</span>
    <a class="btn btn-small" href="#">View Details</a>
  </div>
  <div class="abs ring" style="left:736px;top:190px"><div class="face" role="img" aria-label="Portrait of a male attorney" style="background:linear-gradient(160deg,#C9A68C,#3A2A22)"></div></div>
</section>

<section class="section blog">
  <div class="eyebrow">Blog</div>
  <h2 class="section-title">Latest News &amp; Blog</h2>
  <div class="abs posts">
    <article class="post">
      <div class="thumb" role="img" aria-label="Semi truck on a highway" style="background:linear-gradient(135deg,#B94A4E,#4A2A2E)"><div class="date">12<br>JUN</div></div>
      <h3>Trucking Company Offers A Bigger Settlement</h3>
      <a class="btn btn-small" href="#">Read More</a>
    </article>
    <article class="post">
      <div class="thumb" role="img" aria-label="Officer speaking with a driver at a roadside stop" style="background:linear-gradient(135deg,#8E98A6,#3A4250)"><div class="date">08<br>JUN</div></div>
      <h3>DUI Driver Ordered to Pay Victim’s Costs</h3>
      <a class="btn btn-small" href="#">Read More</a>
    </article>
    <article class="post">
      <div class="thumb" role="img" aria-label="Cars crashed at a city intersection" style="background:linear-gradient(135deg,#A8A29A,#4E4A44)"><div class="date">02<br>JUN</div></div>
      <h3>Settlement Reached in Nashville Rear-End Case</h3>
      <a class="btn btn-small" href="#">Read More</a>
    </article>
  </div>
</section>

<footer class="section footer">
  <h2 class="abs">Contact Us</h2>
  <div class="abs rule"></div>
  <div class="abs addr">Head Office<br>1046 Larkspur Avenue<br>Nashville, TN 37209<br>Tennessee, USA</div>
  <div class="abs" style="left:230px;top:250px;display:flex;flex-direction:column;gap:12px">
    <div class="contact-line"><svg width="14" height="10" viewBox="0 0 14 10"><rect x=".5" y=".5" width="13" height="9" fill="none" stroke="#D8232A"/><path d="M.5 .5 L7 6 L13.5 .5" fill="none" stroke="#D8232A"/></svg>info@pollardlaw-example.com</div>
    <div class="contact-line"><svg width="14" height="14" viewBox="0 0 14 14"><path d="M3 1 L5 1 L6 4 L4.5 5 Q6 8.5 9 9.5 L10 8 L13 9 L13 11 Q13 13 11 13 Q2 12 1 3 Q1 1 3 1 Z" fill="#D8232A"/></svg>(615) 555-0148</div>
    <div class="contact-line"><svg width="14" height="14" viewBox="0 0 14 14"><path d="M3 1 L5 1 L6 4 L4.5 5 Q6 8.5 9 9.5 L10 8 L13 9 L13 11 Q13 13 11 13 Q2 12 1 3 Q1 1 3 1 Z" fill="#D8232A"/></svg>(615) 555-0192</div>
  </div>
  <div class="abs socials"><span></span><span></span><span></span><span></span></div>
  <form class="abs form">
    <div class="field">Your Name</div>
    <div class="field">Email Address</div>
    <div class="field">Phone Number</div>
    <div class="field">Subject</div>
    <div class="field tall">Message</div>
    <small>By submitting this form you agree that no attorney-client relationship is formed and that your details will be kept private.</small>
    <span class="submit">Submit Now</span>
  </form>
</footer>

<div class="section copyright">©2021 Pollard Law Firm PLLC All Rights Reserved</div>

</body>
</html>
```